Fenwick Rise Website Using Wordpress Jetpack CMS

Design a responsive SEO enabled website using Wordpress theme. 7 Pages with content to be developed. Primarily a single page site using Wordpress, so seeking a string website developer with capable skills in native understanding of SEO.

Unique Value Proposition
Sports Clubs are built on passion, people and facilities. All the volunteering and dedication in the world is limited by the level of quality services and benefits that are available to member. Access to funds and lack of knowledge create a void that holds back Club growth and access to improved facilities. Improved facilities draw members and discretionary spend to clubs, but Clubs are challenged in easily delivering expensive facility upgrades. We solve that problem in a way that's easy to digest and meets all the things considered and many that have not been considered at all!

High Level Concept
Fenwick Rise seeks to solve a growing problem. How do clubs remain viable? How do clubs increase participation? How do clubs provide exceptional value for their members discretionary expenditure?

The heart of any solid sporting club is its people, volunteers all over the world, trying to make a difference.

Fenwick Rise was built to facilitate Club growth by providing state of the art facilities without any capital exposure, in fact by providing a shared revenue model that allows for additional facilities to be layered on top of existing ones. Linking in an energy transfer scheme from the excess energy released in peak, the model allows extension to Club Member Energy Offers which exponentially grows revenues and provides strong fiscal opportunity back to the club.

At the centre of Fenwick rise are Lights and Power which are a primary life blood of every club, particularly sports clubs offering training and coaching, like tennis, soccer, rugby lawn bowls, cricket and aussie rules to name a few

With energy bills reaching in excess of $10,000 per annum in many clubs, Fenwick Rise aims to facilitate an energy performance contract for sports clubs that provides new facilities without financial exposure and a profit share on asset placement. This makes decision making easier for volunteer committees

Problems in Clubs
Membership and Participation
Attracting members and ensuring they get appropriate bang for buck takes time, energy and resources. Members seek quality environments with structured sport and easy access to sport facilities at times that suit.

Funding of Capital Assets
Clubs have considerable expenditure in infrastructure to ensure high quality facilities are upgraded and maintained.

Managing The Club
Clubs have considerable expenditure in day to day costs and unpaid volunteers are needed to maintain membership numbers and ensure high quality facilities and available.

The Solution
COST NEUTRAL INFRASTRUCTURE
Assess Power Expenditure
Identify Facilities Improvements - Value Adds etc
Provide Best Outcome Funding Model (Off Grid), Future Asset Returns, Booking/Club Mgnt
Deploy and Maintain Assets, Lower Maintenance

NEXT GEN ENERGY RETAIL SPONSORSHIP
Recover KOLR credits
Negotiate on Grid Sales
Develop Finance and Energy Rebates
Leverage Trading Mechanism

CLUB & MEMBER BENEFITS
Sponsor through Energy Purchase
Members Benefits in Offset Costs and Club Kickback
Giving Back drives the Club Improvement Plan and Income Generation + Carbon Neutral

Target Market(s)

Sports Clubs, Sports Club Committees, Local Councils looking to upgrade local club facilities

Coding

Coded - Design and coding required

Number of Pages Required

5+ page

Font styles to use
Sans Serif

Colors
acd036
848484

Requirements
Must have
• Responsive Design
• Must use Wordpress Jetpack for Delivery
• Target to use Theme with single page
• CMS for custom content additions
• Existing Domain
• Landing Pages
Nice to have
• https://www.quennary.com/en_AU/brightoak is an example of a site that displays characteristics
• Clean colour per logo and ability to expand easily using Wordpress
Should not have
• Hardcoded elements. CMS is a MUST HAVE

```html
<!DOCTYPE html>
<html lang="en">
<head>
<meta charset="utf-8">
<title>Fenwick Rise – Lighting Up Sport</title>
<link rel="stylesheet" href="https://fonts.googleapis.com/css2?family=Cormorant+Garamond:ital,wght@0,500;0,600;0,700;1,500&family=Arimo:wght@400&family=Open+Sans:wght@400;600&display=swap">
<style>
  :root{
    --green:#54931a;
    --green-dark:#4a8414;
    --grey:#848484;
    --ink:#1f1f1f;
    --text:#333333;
    --white:#ffffff;
    --light:#ececec;
    --footer:#4d4d4d;
    --icon:#6a6a6a;
  }
  *{margin:0;padding:0;box-sizing:border-box}
  html,body{width:1200px;height:2675px;overflow:hidden}
  body{position:relative;background:var(--white);font-family:"Arimo",Arial,sans-serif;color:var(--text)}
  .abs{position:absolute}

  /* Hero */
  .hero{left:0;top:0;width:1200px;height:620px;overflow:hidden}
  .hero-photo{position:absolute;inset:0;background:
      radial-gradient(ellipse 160px 140px at 60px 120px,rgba(255,255,255,.85),transparent 70%),
      radial-gradient(ellipse 160px 140px at 1140px 120px,rgba(255,255,255,.85),transparent 70%),
      linear-gradient(180deg,#1b3f9a 0%,#2e63c4 30%,#6f9bd8 55%,#1f3c7a 72%,#0d1f45 100%)}
  .brand{left:98px;top:30px;font-family:"Cormorant Garamond",serif;font-weight:700;font-size:46px;color:#9bcf3a;letter-spacing:1px}
  .nav{left:0;top:47px;width:1200px;height:20px}
  .nav a{position:absolute;font-family:"Cormorant Garamond",serif;font-weight:700;font-size:14px;color:var(--white);text-decoration:none;letter-spacing:.5px;transform:translateX(-50%)}
  .search{left:1087px;top:49px}
  .hero-kicker{left:0;width:1200px;top:212px;text-align:center;font-family:"Cormorant Garamond",serif;font-weight:500;font-size:44px;color:var(--white);font-variant:small-caps;letter-spacing:2px}
  .hero-title{left:0;width:1200px;top:285px;text-align:center;font-family:"Cormorant Garamond",serif;font-weight:500;font-size:58px;color:var(--white);letter-spacing:2px}
  .slide-arrow{top:244px;width:50px;height:50px}
  .hero-curve{left:0;top:540px}

  /* About */
  .about-title{left:100px;top:698px;font-family:"Cormorant Garamond",serif;font-weight:600;font-size:33px;color:var(--ink);letter-spacing:1px}
  .about-sub{left:100px;top:749px;font-family:"Cormorant Garamond",serif;font-weight:700;font-size:12px;color:var(--green);letter-spacing:.3px}
  .about-text{left:100px;top:790px;width:500px;font-size:15px;line-height:27.5px;color:var(--text)}
  .btn-more{left:100px;top:987px;width:158px;height:44px;border-radius:22px;background:var(--green);color:var(--white);font-family:"Cormorant Garamond",serif;font-weight:700;font-size:16px;font-variant:small-caps;display:flex;align-items:center;justify-content:center;letter-spacing:.5px}
  .gallery-box{left:742px;top:704px;width:358px;height:419px;background:var(--green)}
  .gallery-main{left:688px;top:754px;width:366px;height:255px;border:3px solid var(--white);background:linear-gradient(135deg,#3a3a3a,#151515 55%,#b01b1b 80%,#2a2a2a)}
  .thumb{top:1018px;height:57px}
  .gallery-nav{left:756px;top:1090px}

  /* Supply */
  .supply{left:0;top:1207px;width:1200px;height:644px;background:
      radial-gradient(ellipse 300px 200px at 150px 200px,rgba(255,255,255,.7),transparent 70%),
      radial-gradient(ellipse 300px 200px at 1050px 200px,rgba(255,255,255,.7),transparent 70%),
      linear-gradient(180deg,#c9dcee 0%,#e6eef4 40%,#b7c4cc 80%,#9aa7ae 100%)}
  .supply-title{left:0;width:1200px;top:1305px;text-align:center;font-family:"Cormorant Garamond",serif;font-weight:600;font-size:29px;color:var(--ink);letter-spacing:1px}
  .supply-text{left:0;width:1200px;top:1362px;text-align:center;font-family:"Cormorant Garamond",serif;font-style:italic;font-weight:500;font-size:15px;line-height:27px;color:#333}
  .card{width:298px;height:283px;border-radius:34px;overflow:hidden}
  .card-photo{position:absolute;inset:0}
  .card-label{position:absolute;left:0;bottom:0;width:100%;height:61px;background:rgba(20,20,20,.82);display:flex;align-items:center;justify-content:center;font-family:"Cormorant Garamond",serif;font-weight:600;font-size:18px;color:var(--white);letter-spacing:.5px}
  .card-white{background:var(--white)}
  .card-white .card-label{background:transparent;color:var(--ink)}

  /* Booking */
  .booking{left:0;top:1851px;width:1200px;height:390px;background:var(--green)}
  .booking-curve{left:0;top:2236px}
  .booking-title{left:0;width:1200px;top:1919px;text-align:center;font-family:"Cormorant Garamond",serif;font-weight:700;font-size:31px;color:var(--white);letter-spacing:1px}
  .field{height:39px;background:var(--white);font-family:"Open Sans",sans-serif;font-size:13px;color:#444;display:flex;align-items:center;padding-left:14px;padding-right:16px;justify-content:space-between}
  .btn-book{left:537px;top:2156px;width:126px;height:43px;border:1.5px solid var(--white);border-radius:22px;color:var(--white);font-family:"Cormorant Garamond",serif;font-weight:700;font-size:16px;display:flex;align-items:center;justify-content:center;letter-spacing:.5px}

  /* Contact */
  .contact{left:0;top:2236px;width:1200px;height:314px;background:var(--light)}
  .contact-icon{top:2343px;width:78px;height:78px}
  .contact-text{top:2436px;width:300px;text-align:center;font-family:"Open Sans",sans-serif;font-size:13px;line-height:23px;color:#222}

  /* Footer */
  .footer-nav{left:0;top:2550px;width:1200px;height:62px;background:var(--light);border-top:1px solid #cfcfcf}
  .footer-nav span{position:absolute;top:19px;font-family:"Open Sans",sans-serif;font-size:13.5px;color:#222;transform:translateX(-50%)}
  .copyright{left:0;top:2612px;width:1200px;height:63px;background:var(--footer);color:var(--white);font-family:"Open Sans",sans-serif;font-size:13px;display:flex;align-items:center;justify-content:center}
</style>
</head>
<body>

<header class="abs hero">
  <div class="hero-photo" role="img" aria-label="Floodlit sports stadium at night with a packed crowd"></div>
  <div class="abs brand">Fenwick Rise</div>
  <nav class="abs nav">
    <a style="left:567px">HOME</a>
    <a style="left:660px">ABOUT</a>
    <a style="left:763px">SERVICES</a>
    <a style="left:874px">BOOKING</a>
    <a style="left:995px">CONTACT US</a>
  </nav>
  <svg class="abs search" width="16" height="16" viewBox="0 0 16 16" aria-label="Search"><circle cx="6.5" cy="6.5" r="4.5" fill="none" stroke="#fff" stroke-width="2"/><line x1="10" y1="10" x2="14" y2="14" stroke="#fff" stroke-width="2.4" stroke-linecap="round"/></svg>
  <div class="abs hero-kicker">Fenwick Rise</div>
  <h1 class="abs hero-title">LIGHTING UP SPORT</h1>
  <svg class="abs slide-arrow" style="left:59px" viewBox="0 0 50 50" aria-label="Previous slide"><circle cx="25" cy="25" r="24" fill="var(--green)"/><path d="M36 25H16M24 15l-10 10 10 10" fill="none" stroke="#fff" stroke-width="6" stroke-linejoin="round"/></svg>
  <svg class="abs slide-arrow" style="left:1091px" viewBox="0 0 50 50" aria-label="Next slide"><circle cx="25" cy="25" r="24" fill="var(--green)"/><path d="M14 25h20M26 15l10 10-10 10" fill="none" stroke="#fff" stroke-width="6" stroke-linejoin="round"/></svg>
  <svg class="abs hero-curve" width="1200" height="80" viewBox="0 0 1200 80" aria-hidden="true">
    <path d="M0 58 Q600 -2 1200 64 L1200 80 L0 80Z" fill="var(--green)"/>
    <path d="M0 68 Q600 18 1200 70 L1200 80 L0 80Z" fill="#fff"/>
  </svg>
</header>

<section class="about">
  <h2 class="abs about-title">ABOUT US</h2>
  <div class="abs about-sub">GET TO KNOW US FROM OUR VIDEO</div>
  <p class="abs about-text">Lorem ipsum dolor sit amet, consectetur adipiscing elit, sed do eiusmod tempor incididunt ut labore et dolore magna aliqua. Ut enim ad minim veniam, quis nostrud exercitation ullamco laboris nisi ut aliquip ex ea commodo consequat. Duis aute irure dolor in reprehenderit in voluptate velit esse cillum dolore eu fugiat nulla pariatur. Excepteur sint occaecat cupidatat non proident, sunt in culpa qui officia deserunt mollit anim id est laborum</p>
  <div class="abs btn-more">Know More &gt;&gt;</div>
  <div class="abs gallery-box"></div>
  <div class="abs gallery-main" role="img" aria-label="Hand attaching a red clamp to a car battery terminal"></div>
  <div class="abs thumb" style="left:688px;width:84px;background:linear-gradient(180deg,#1d3563,#5d7fa8)" role="img" aria-label="Stadium under lights"></div>
  <div class="abs thumb" style="left:781px;width:85px;background:linear-gradient(135deg,#2a5f3a,#6e8d52)" role="img" aria-label="Worker installing solar panels"></div>
  <div class="abs thumb" style="left:875px;width:86px;background:linear-gradient(180deg,#0f1c3a,#6e8fd0)" role="img" aria-label="Floodlights at night"></div>
  <div class="abs thumb" style="left:970px;width:85px;background:linear-gradient(135deg,#4a6fae,#c04a3a)" role="img" aria-label="Technician on a roof with panels"></div>
  <svg class="abs gallery-nav" width="52" height="24" viewBox="0 0 52 24" aria-label="Gallery navigation"><path d="M2 12h16M2 12l5-4M2 12l5 4M34 12h16M50 12l-5-4M50 12l-5 4" fill="none" stroke="#fff" stroke-width="2"/><line x1="26" y1="3" x2="26" y2="21" stroke="#fff" stroke-width="2"/></svg>
</section>

<section class="abs supply" role="img" aria-label="Soft daytime stadium backdrop"></section>
<h2 class="abs supply-title">WE SUPPLY</h2>
<p class="abs supply-text">Sed ut perspiciatis unde omnis iste natus error sit voluptatem accusantium doloremque laudantium,<br>totam rem aperiam, eaque ipsa quae ab illo inventore veritatis</p>
<div class="abs card" style="left:100px;top:1450px">
  <div class="card-photo" role="img" aria-label="Hanging glass pendant light bulbs" style="background:linear-gradient(135deg,#5a3a2a,#2b2b2b 45%,#c89a4a 75%,#3a3a3a)"></div>
  <div class="card-label">ART LIGHTS</div>
</div>
<div class="abs card" style="left:449px;top:1475px">
  <div class="card-photo" role="img" aria-label="Solar panels on a house roof" style="background:linear-gradient(160deg,#3c5a8c,#7f95b8 45%,#9a7a52 75%,#4a5a3a)"></div>
  <div class="card-label">SOLAR</div>
</div>
<div class="abs card card-white" style="left:800px;top:1450px">
  <div class="card-photo" role="img" aria-label="Car battery product shot" style="background:radial-gradient(ellipse 110px 80px at 50% 38%,#9a9a9a,#fff 80%)"></div>
  <div class="card-label">BATTERY TECHNOLOGY</div>
</div>

<section class="abs booking"></section>
<section class="abs contact"></section>
<svg class="abs booking-curve" width="1200" height="50" viewBox="0 0 1200 50" aria-hidden="true"><path d="M0 0H1200V2 Q600 90 0 2Z" fill="var(--green)"/></svg>
<h2 class="abs booking-title">FOR ONLINE BOOKING</h2>
<div class="abs field" style="left:251px;top:2002px;width:330px">Name</div>
<div class="abs field" style="left:612px;top:2002px;width:337px">Phone Number</div>
<div class="abs field" style="left:251px;top:2070px;width:330px">Organisation
  <svg width="10" height="6" viewBox="0 0 10 6"><path d="M0 0h10L5 6z" fill="#444"/></svg></div>
<div class="abs field" style="left:612px;top:2070px;width:337px">Schedule your date
  <svg width="13" height="13" viewBox="0 0 13 13"><rect x="1" y="2" width="11" height="10" fill="none" stroke="#555" stroke-width="1.4"/><rect x="1" y="2" width="11" height="3" fill="#555"/><rect x="3.5" y="7" width="2" height="2" fill="#555"/><rect x="7.5" y="7" width="2" height="2" fill="#555"/></svg></div>
<div class="abs btn-book">BOOK NOW</div>

<svg class="abs contact-icon" style="left:198px" viewBox="0 0 78 78" aria-label="Address"><circle cx="39" cy="39" r="39" fill="var(--icon)"/><path d="M39 57s-11-12-11-21a11 11 0 0 1 22 0c0 9-11 21-11 21z" fill="none" stroke="#fff" stroke-width="2"/><circle cx="39" cy="36" r="4" fill="none" stroke="#fff" stroke-width="2"/></svg>
<svg class="abs contact-icon" style="left:560px" viewBox="0 0 78 78" aria-label="Phone"><circle cx="39" cy="39" r="39" fill="var(--icon)"/><path d="M28 27c2-2 4-2 5 0l2 4c1 2 0 3-1 4 1 3 4 6 7 7 1-1 2-2 4-1l4 2c2 1 2 3 0 5-4 4-10 1-16-5s-9-12-5-16z" fill="none" stroke="#fff" stroke-width="2"/><path d="M42 26a10 10 0 0 1 10 10M42 31a5 5 0 0 1 5 5" fill="none" stroke="#fff" stroke-width="2"/></svg>
<svg class="abs contact-icon" style="left:920px" viewBox="0 0 78 78" aria-label="Email"><circle cx="39" cy="39" r="39" fill="var(--icon)"/><rect x="26" y="30" width="26" height="18" fill="none" stroke="#fff" stroke-width="2"/><path d="M26 30l13 11 13-11M26 48l10-9M52 48l-10-9" fill="none" stroke="#fff" stroke-width="2"/></svg>
<p class="abs contact-text" style="left:87px">#123 Building Name,<br>Street Name,City Location,<br>Zip Code.</p>
<p class="abs contact-text" style="left:449px;top:2440px">123-456-7899</p>
<p class="abs contact-text" style="left:809px">info@fenwickrise.com</p>

<footer>
  <nav class="abs footer-nav">
    <span style="left:218px">Home</span><span style="left:285px">|</span>
    <span style="left:365px">About Us</span><span style="left:442px">|</span>
    <span style="left:519px">Services</span><span style="left:594px">|</span>
    <span style="left:670px">Projects</span><span style="left:745px">|</span>
    <span style="left:824px">Bookings</span><span style="left:902px">|</span>
    <span style="left:977px">Contact</span>
  </nav>
  <div class="abs copyright">Copyright © 2018 Fenwick Rise . All rights reserved</div>
</footer>

</body>
</html>
```